Business Card Design

We Need a business card design for my company based in Tv Radio and music Productions and hunt Talent.

Industry/Entity Type

Business

Contact Information for Business Card

BrentaVue Production's, Teodor Vignoles,Cell Phone 318 4957310
Musician, Productor, Hunt Talent. Miami Fla. www.brentavue.net Mail. teodorvignoles@mailvana.com

```html
<!DOCTYPE html>
<html lang="en">
<head>
<meta charset="utf-8">
<title>BrentaVue Productions – Business Card</title>
<link rel="stylesheet" href="https://fonts.googleapis.com/css2?family=Yellowtail&family=Mulish:wght@400;800&display=swap">
<style>
  :root {
    --bg: #e4e4e2;
    --sky-center: #e6f7fd;
    --sky-mid: #7fd0f2;
    --sky-edge: #18a6e0;
    --sun-center: #fff6c9;
    --sun-edge: #fddd3c;
    --red: #c8232c;
    --purple: #6a3aa0;
    --ink: #2a2a2a;
    --card-shadow: 0 14px 30px rgba(0,0,0,.22);
  }
  * { margin: 0; padding: 0; box-sizing: border-box; }
  html, body { width: 1200px; height: 1000px; overflow: hidden; }
  body {
    background: var(--bg);
    position: relative;
    font-family: "Mulish", sans-serif;
  }
  .card {
    position: absolute;
    box-shadow: var(--card-shadow);
    overflow: hidden;
  }
  /* Front */
  .card-front {
    left: 90px; top: 220px;
    width: 380px; height: 560px;
    background: radial-gradient(circle at 50% 42%, var(--sky-center) 0%, var(--sky-mid) 35%, var(--sky-edge) 75%);
  }
  .front-mark {
    position: absolute;
    left: 0; right: 0; top: 190px;
    display: flex; align-items: center; justify-content: center; gap: 14px;
  }
  .mark-dot {
    width: 44px; height: 44px; border-radius: 50%;
    background: var(--sun-edge);
  }
  .brand-name {
    font-family: "Mulish", sans-serif;
    font-weight: 800;
    font-size: 46px;
    color: var(--red);
  }
  .front-url {
    position: absolute;
    left: 0; right: 0; top: 270px;
    text-align: center;
    font-weight: 800;
    font-size: 20px;
    color: var(--purple);
  }
  /* Back */
  .card-back {
    left: 540px; top: 310px;
    width: 580px; height: 380px;
    background: radial-gradient(circle at 52% 40%, var(--sun-center) 0%, #fde98a 30%, var(--sun-edge) 70%);
    padding: 48px 40px 0 70px;
  }
  .studio-name {
    font-family: "Yellowtail", cursive;
    font-size: 38px;
    color: var(--red);
    text-align: center;
  }
  .person-name {
    font-family: "Yellowtail", cursive;
    font-size: 42px;
    color: var(--purple);
    text-align: center;
    margin-top: 2px;
  }
  .person-role {
    font-weight: 800;
    font-size: 17px;
    color: var(--ink);
    text-align: center;
    margin-top: 4px;
  }
  .contact {
    margin-top: 18px;
    list-style: none;
    font-size: 18px;
    color: var(--ink);
    line-height: 1.45;
  }
  .contact .web { font-weight: 800; }
</style>
</head>
<body>
  <section class="card card-front" aria-label="Card front">
    <div class="front-mark">
      <span class="mark-dot" aria-hidden="true"></span>
      <span class="brand-name">BrentaVue</span>
    </div>
    <p class="front-url">www.brentavue.net</p>
  </section>

  <section class="card card-back" aria-label="Card back">
    <h1 class="studio-name">BrentaVue Productions</h1>
    <h2 class="person-name">Teodor Vignoles</h2>
    <p class="person-role">Musician, Producer, Talent Hunter</p>
    <ul class="contact">
      <li>Cell Phone 318 4957310 Miami, Florida</li>
      <li class="web">www.brentavue.net</li>
      <li>Mail: teodorvignoles@mailvana.com</li>
    </ul>
  </section>
</body>
</html>
```